Packaging Design for Natural Skin Care Black Soap Coconut Milk Line

Marula Grove is developing a line of Natural Black Soap Coconut Milk Skin care products. These products include a Bar Soap, Body Wash, Body Butter, Body Lotion. As well as Hair Care – shampoo , conditioner, mask & detangler. This will be an ever expanding line so the list will go on and on. We are looking to stay consistent with our current brand design but would like to give a sleeker, sexy, black look. Attached are some of our current label designs and product images.

```html
<!DOCTYPE html>
<html lang="en">
<head>
<meta charset="utf-8">
<title>Marula Grove Shampoo Label</title>
<link href="https://fonts.googleapis.com/css2?family=Josefin+Sans:wght@300;400&family=Montserrat:wght@400;600&display=swap" rel="stylesheet">
<style>
  :root {
    --page-bg: #ffffff;
    --label-black: #151515;
    --label-edge: #0b0b0b;
    --ink-silver: #e6e6e6;
    --ink-soft: #bdbdbd;
    --badge-grey: #cfcfcf;
  }
  html, body {
    margin: 0;
    padding: 0;
    width: 1035px;
    height: 1200px;
    overflow: hidden;
    background: var(--page-bg);
  }
  .canvas {
    position: relative;
    width: 1035px;
    height: 1200px;
  }
  .label {
    position: absolute;
    left: 380px;
    top: 505px;
    width: 265px;
    height: 525px;
    background: radial-gradient(ellipse at 50% 40%, #1d1d1d 0%, var(--label-black) 55%, var(--label-edge) 100%);
    color: var(--ink-silver);
    font-family: "Montserrat", sans-serif;
    text-align: center;
  }
  .label > * {
    position: absolute;
    left: 0;
    width: 100%;
    margin: 0;
  }
  .brand {
    top: 68px;
    display: flex;
    justify-content: center;
    align-items: center;
    gap: 7px;
    font-family: "Montserrat", sans-serif;
    font-weight: 400;
    font-size: 19px;
    color: var(--ink-silver);
  }
  .brand-dot {
    width: 10px;
    height: 10px;
    border-radius: 50%;
    background: var(--ink-silver);
  }
  .seal {
    top: 128px;
    height: 96px;
  }
  .tagline {
    top: 244px;
    font-family: "Josefin Sans", sans-serif;
    font-weight: 300;
    font-size: 13px;
    color: var(--ink-soft);
  }
  .product-name {
    top: 262px;
    font-family: "Josefin Sans", sans-serif;
    font-weight: 400;
    font-size: 37px;
    letter-spacing: 1px;
    color: var(--ink-silver);
  }
  .ingredient {
    top: 302px;
    font-family: "Josefin Sans", sans-serif;
    font-weight: 300;
    font-size: 13px;
    color: var(--ink-soft);
  }
  .detail-heading {
    top: 343px;
    font-family: "Montserrat", sans-serif;
    font-weight: 400;
    font-size: 14px;
    letter-spacing: 0.5px;
  }
  .detail-copy {
    top: 366px;
    left: 28px;
    width: 209px;
    font-size: 7.2px;
    line-height: 1.3;
    text-align: center;
    color: var(--ink-silver);
  }
  .usp-list {
    top: 446px;
    font-weight: 600;
    font-size: 9px;
    letter-spacing: 0.3px;
  }
  .volume {
    top: 473px;
    font-weight: 400;
    font-size: 18px;
  }
</style>
</head>
<body>
<main class="canvas">
  <section class="label">
    <div class="brand"><span class="brand-dot"></span><span>Marula Grove</span></div>
    <svg class="seal" viewBox="0 0 265 96" role="img" aria-label="100% natural seal badge">
      <circle cx="132.5" cy="48" r="44" fill="none" stroke="var(--badge-grey)" stroke-width="2"/>
    </svg>
    <p class="tagline">some text here</p>
    <h1 class="product-name">SHAMPOO</h1>
    <p class="ingredient">with shea butter</p>
    <h2 class="detail-heading">SHAMPOO DETAIL</h2>
    <p class="detail-copy">Lorem ipsum dolor sit amet, consectetur adipisicing elit, sed do eiusmod tempor incididunt ut labore et dolore magna aliqua. Ut enim ad minim veniam, quis nostrud exercitation.</p>
    <p class="usp-list">USP 1 | USP 2 | USP 3</p>
    <p class="volume">8 fl. oz (236 ml)</p>
  </section>
</main>
</body>
</html>
```